New Alcoholic Spiked Seltzer Line

We need a can design for a line of low calorie alcoholic seltzer. This product is a sparkling water and vodka drink with no sugar added in a slim 12 oz can.

This is a lighter, healthier, alternative to the sugary ready-to-drinks on the market. The product contains only 3 ingredients: Vodka, Water and Natural Flavors. It has only 100 calories but still has 5% alcohol, so you don't need to sacrifice alcohol to cut calories.

This product also does not contain any preservatives.

We want this design to communicate the following objectives to the consumer and in this order:

1. Appetizing product
2.Low calorie
3.Communicate the type of beverage (Spiked Seltzer)

The brand name of the product is VELKA.

The flavor of the product needed to be used for the design is Mango-Orange.

Comparable products are:

www.brisavelfizz.example/
https://www.tarnowbubble.example
https://quellrind.example/

The designs should not infringe or copy the creative directions of the products mentionned above. They are only given so that you can better understand the type of product we are developing.

Target Market(s)

Young Professional women between the ages of 25 and 44

Industry/Entity Type

Product

Colors

Designer to choose colors to be used in the design.

Requirements
Must have
• Design extendibility, meaning it can be adapted for other flavors.
• This is a new category in the market we are targeting, so consumers must easily be able to identify what type of product this is.

```html
<!DOCTYPE html>
<html lang="en">
<head>
<meta charset="utf-8">
<title>VELKA Spiked Seltzer – Flavour Labels</title>
<link rel="stylesheet" href="https://fonts.googleapis.com/css2?family=Josefin+Sans:wght@300;400&family=Open+Sans:wght@300;400&display=swap">
<style>
  :root {
    --stage-top: #fbfbfb;
    --stage-bottom: #e9e9e9;
    --ink: #ffffff;
    --teal: #8fd8cf;
    --teal-leaf: #3f6a6e;
    --pink: #fcc6dc;
    --pink-leaf: #5a4a66;
    --mint: #b2dfcc;
    --mint-leaf: #44686a;
    --sand: #d3c599;
    --sand-leaf: #5c5a45;
  }
  * { box-sizing: border-box; margin: 0; padding: 0; }
  html, body {
    width: 1200px; height: 683px; overflow: hidden;
  }
  body {
    position: relative;
    background: linear-gradient(180deg, var(--stage-top), var(--stage-bottom));
    font-family: "Open Sans", Arial, sans-serif;
    color: var(--ink);
  }
  .label {
    position: absolute;
    background: var(--base);
    box-shadow: 0 6px 8px rgba(0,0,0,0.18);
    overflow: hidden;
  }
  .label--teal { left: 98px;  top: 95px; width: 227px; height: 495px; --base: var(--teal); --leaf: var(--teal-leaf); }
  .label--pink { left: 346px; top: 95px; width: 228px; height: 495px; --base: var(--pink); --leaf: var(--pink-leaf); }
  .label--mint { left: 597px; top: 94px; width: 229px; height: 497px; --base: var(--mint); --leaf: var(--mint-leaf); }
  .label--sand { left: 846px; top: 91px; width: 232px; height: 503px; --base: var(--sand); --leaf: var(--sand-leaf); }

  .label__foliage {
    position: absolute; left: 0; top: 0; width: 100%; height: 140px;
    background: linear-gradient(180deg, var(--leaf) 0%, var(--leaf) 35%, transparent 100%);
    opacity: 0.85;
  }
  .label__brand {
    position: absolute; left: 0; right: 0; top: 122px;
    text-align: center;
    font-family: "Josefin Sans", Arial, sans-serif;
    font-weight: 400;
    font-size: 46px; line-height: 46px;
    letter-spacing: 10px; padding-left: 10px;
  }
  .label__rule {
    position: absolute; left: 50%; width: 72px; height: 2px;
    margin-left: -36px; background: var(--ink);
  }
  .label__rule--brand { top: 184px; }
  .label__rule--taste { top: 328px; }
  .label__descriptor {
    position: absolute; left: 0; right: 0; top: 206px;
    text-align: center;
    font-weight: 300; font-size: 12px; line-height: 14px;
    letter-spacing: -0.3px;
  }
  .label__flavour {
    position: absolute; left: 0; right: 0; top: 297px;
    text-align: center;
    font-weight: 400; font-size: 14px; line-height: 18px;
  }
  .label__stat {
    position: absolute; left: 0; right: 0; height: 20px;
    display: flex; align-items: center;
    font-family: "Josefin Sans", Arial, sans-serif;
    font-weight: 300; font-size: 10px; text-transform: uppercase;
  }
  .label__stat--calories { top: 371px; }
  .label__stat--alcohol { top: 391px; }
  .stat__bar { height: 4px; background: var(--ink); }
  .stat__line { height: 2px; background: var(--ink); }
  .label__stat--calories .stat__bar:first-child { width: 24%; }
  .label__stat--calories .stat__text { flex: 1; text-align: center; }
  .label__stat--calories .stat__bar:last-child { width: 19%; }
  .label__stat--alcohol .stat__line:first-child { width: 43%; }
  .label__stat--alcohol .stat__text { flex: 1; text-align: center; }
  .label__stat--alcohol .stat__line:last-child { width: 10%; }
  .stat__figure { font-size: 19px; font-weight: 300; vertical-align: -2px; }
  .stat__percent { font-size: 15px; vertical-align: -1px; }
</style>
</head>
<body>
  <main class="label-range">
    <section class="label label--teal">
      <div class="label__foliage" role="img" aria-label="Palm fronds hanging from the top edge, tinted dark teal"></div>
      <h1 class="label__brand">VELKA</h1>
      <div class="label__rule label__rule--brand"></div>
      <p class="label__descriptor">sparkling water &amp; vodka drink<br>with no added sugar</p>
      <p class="label__flavour">TASTE</p>
      <div class="label__rule label__rule--taste"></div>
      <div class="label__stat label__stat--calories"><span class="stat__bar"></span><span class="stat__text">only<span class="stat__figure">100</span>calories</span><span class="stat__bar"></span></div>
      <div class="label__stat label__stat--alcohol"><span class="stat__line"></span><span class="stat__text"><span class="stat__percent">5%</span> alcohol</span><span class="stat__line"></span></div>
    </section>

    <section class="label label--pink">
      <div class="label__foliage" role="img" aria-label="Palm fronds hanging from the top edge, tinted plum"></div>
      <h2 class="label__brand">VELKA</h2>
      <div class="label__rule label__rule--brand"></div>
      <p class="label__descriptor">sparkling water &amp; vodka drink<br>with no added sugar</p>
      <p class="label__flavour">TASTE</p>
      <div class="label__rule label__rule--taste"></div>
      <div class="label__stat label__stat--calories"><span class="stat__bar"></span><span class="stat__text">only<span class="stat__figure">100</span>calories</span><span class="stat__bar"></span></div>
      <div class="label__stat label__stat--alcohol"><span class="stat__line"></span><span class="stat__text"><span class="stat__percent">5%</span> alcohol</span><span class="stat__line"></span></div>
    </section>

    <section class="label label--mint">
      <div class="label__foliage" role="img" aria-label="Palm fronds hanging from the top edge, tinted slate green"></div>
      <h2 class="label__brand">VELKA</h2>
      <div class="label__rule label__rule--brand"></div>
      <p class="label__descriptor">sparkling water &amp; vodka drink<br>with no added sugar</p>
      <p class="label__flavour">TASTE</p>
      <div class="label__rule label__rule--taste"></div>
      <div class="label__stat label__stat--calories"><span class="stat__bar"></span><span class="stat__text">only<span class="stat__figure">100</span>calories</span><span class="stat__bar"></span></div>
      <div class="label__stat label__stat--alcohol"><span class="stat__line"></span><span class="stat__text"><span class="stat__percent">5%</span> alcohol</span><span class="stat__line"></span></div>
    </section>

    <section class="label label--sand">
      <div class="label__foliage" role="img" aria-label="Palm fronds hanging from the top edge, tinted olive brown"></div>
      <h2 class="label__brand">VELKA</h2>
      <div class="label__rule label__rule--brand"></div>
      <p class="label__descriptor">sparkling water &amp; vodka drink<br>with no added sugar</p>
      <p class="label__flavour">TASTE</p>
      <div class="label__rule label__rule--taste"></div>
      <div class="label__stat label__stat--calories"><span class="stat__bar"></span><span class="stat__text">only<span class="stat__figure">100</span>calories</span><span class="stat__bar"></span></div>
      <div class="label__stat label__stat--alcohol"><span class="stat__line"></span><span class="stat__text"><span class="stat__percent">5%</span> alcohol</span><span class="stat__line"></span></div>
    </section>
  </main>
</body>
</html>
```